Pinecrest Artisan League Membership

UPDATED files - 06/03/2021
Digital brochure needed for construction contractor related nonprofit organization.
Document will be primarily for digital viewing with potential for print version. Should be branded with our branding (logo attached). This is intended to be a multiple page document, plan to print and web (email) use. Standard Letter size document 8.5 x 11 inch
Portrait format preferred
The attached project brief includes a cover, 4 internal pages, and a back cover. This is flexible pending design layout
Target Market(s)
Residential construction business owners
Requirements
Must have
- See attached brief.Orange color palette: RGB: (253,153,0)
Nice to have
- See attached bief
Should not have
- No suit or ties. button up shirt okay, but not white collar worker.

```html
<!DOCTYPE html>
<html lang="en">
<head>
<meta charset="utf-8">
<title>Pinecrest Artisan League – Membership Brochure</title>
<link href="https://fonts.googleapis.com/css2?family=Outfit:wght@300;400;500;600;700;800&display=swap" rel="stylesheet">
<style>
:root{
  --orange:#fd9900;
  --ink:#2b2b2b;
  --body:#555;
  --bg:#e3e3e3;
  --paper:#ffffff;
  --rule:#dcdcdc;
}
*{margin:0;padding:0;box-sizing:border-box}
html,body{width:1200px;height:3450px;overflow:hidden;background:var(--bg)}
body{position:relative;font-family:"Outfit",sans-serif;color:var(--ink)}
.page{position:absolute;left:371px;width:458px;height:593px;background:var(--paper);overflow:hidden}
.abs{position:absolute}
.h2{font-size:13px;font-weight:500;color:var(--ink)}
.rule{height:1px;background:var(--orange)}
.txt{font-size:6.8px;line-height:10.4px;color:var(--body);font-weight:400}
.txt p{margin-bottom:5px}
.brand{font-weight:800;color:var(--orange);letter-spacing:.2px;white-space:nowrap}
.photo{position:absolute}
.pill{background:var(--orange);color:#fff;border-radius:10px;font-weight:700;font-size:10px;text-align:center;line-height:19px;letter-spacing:.5px}
.ticks{list-style:none;font-size:6.6px;line-height:9px;font-weight:600;color:#555}
.ticks li{position:relative;padding-left:17px;margin-bottom:10px}
.ticks svg{position:absolute;left:0;top:0}
.sub{font-size:7.4px;font-weight:700;color:var(--orange);letter-spacing:.3px}
.footer{position:absolute;left:0;right:0;bottom:0;height:20px;font-size:6px;color:#555}
.footer .site{position:absolute;left:47px;top:4px;white-space:nowrap}
.footer .site::after{content:"";position:absolute;left:0;top:10px;width:98px;height:2px;background:var(--orange)}
.footer .line{position:absolute;left:150px;right:205px;top:7px;height:1px;background:var(--orange)}
.footer .contact{position:absolute;right:46px;top:4px;white-space:nowrap}
.footer.light{color:#fff}
.thumb{position:absolute;width:138px;height:179px;background:var(--paper);overflow:hidden}
.tl-label{position:absolute;font-size:5.8px;font-weight:700;line-height:7px;color:#444}
.skill{position:absolute;left:254px;width:160px;font-size:6.8px;color:#444;border-bottom:1px solid var(--rule);height:26px;line-height:22px;padding-left:34px}
.skill svg{position:absolute;left:6px;top:4px}
</style>
</head>
<body>

<!-- Front cover -->
<div class="thumb" style="left:171px;top:78px">
  <div class="photo" style="left:0;top:0;width:138px;height:143px;background:radial-gradient(ellipse at 55% 45%,#e8b04a 0%,#c98a3a 30%,#7d8e96 65%,#4e5f6a 100%)" role="img" aria-label="Construction workers in hard hats and hi-vis vests reviewing a laptop on site"></div>
  <div class="abs" style="left:9px;top:103px;width:103px;height:40px;background:var(--orange);color:#fff;font-size:6.2px;line-height:7px;font-weight:500;padding:4px 5px">HELPING YOU REDUCE RISKS AND INJURIES WHILE IMPROVING PROFITABILITY</div>
  <div class="abs" style="left:112px;top:100px;width:14px;height:12px;background:#2b2b2b"></div>
  <div class="abs" style="left:13px;top:152px;font-size:3.2px;line-height:5px;color:#666;border-left:1px solid var(--orange);padding-left:3px">pinecrestleague.org<br>hello@pinecrestleague.org<br>555-010-4821</div>
  <div class="abs brand" style="left:80px;top:156px;font-size:4.6px">Pinecrest Artisan League</div>
</div>

<!-- Page 1 -->
<div class="page" style="top:79px">
  <div class="abs" style="left:47px;top:44px;width:155px">
    <div class="h2">Mission</div>
    <div class="rule" style="margin:5px 0 9px"></div>
    <div class="txt">To promote, educate and advance a diverse contractor community by providing pathways of accessibility to help build a stronger foundation for a better future.</div>
    <div class="h2" style="margin-top:28px">Vision</div>
    <div class="rule" style="margin:5px 0 9px"></div>
    <div class="txt">To become the preferred organization for construction contractors striving to be the best in their trade through education, training, and ongoing development.</div>
  </div>
  <div class="abs pill" style="left:47px;top:253px;width:156px">CORE VALUES</div>
  <ul class="abs ticks" style="left:71px;top:292px;width:120px">
    <li><svg width="8" height="8" viewBox="0 0 8 8"><rect x=".5" y=".5" width="7" height="7" fill="none" stroke="#fd9900" stroke-width=".8"/><path d="M1.8 4l1.6 1.6L6.5 2" fill="none" stroke="#fd9900" stroke-width="1"/></svg>Empower through learning and development</li>
    <li><svg width="8" height="8" viewBox="0 0 8 8"><rect x=".5" y=".5" width="7" height="7" fill="none" stroke="#fd9900" stroke-width=".8"/><path d="M1.8 4l1.6 1.6L6.5 2" fill="none" stroke="#fd9900" stroke-width="1"/></svg>Strengthen and sustain the industry</li>
    <li><svg width="8" height="8" viewBox="0 0 8 8"><rect x=".5" y=".5" width="7" height="7" fill="none" stroke="#fd9900" stroke-width=".8"/><path d="M1.8 4l1.6 1.6L6.5 2" fill="none" stroke="#fd9900" stroke-width="1"/></svg>Build partnerships to benefit underserved communities</li>
    <li><svg width="8" height="8" viewBox="0 0 8 8"><rect x=".5" y=".5" width="7" height="7" fill="none" stroke="#fd9900" stroke-width=".8"/><path d="M1.8 4l1.6 1.6L6.5 2" fill="none" stroke="#fd9900" stroke-width="1"/></svg>Act with integrity, respect, and honesty</li>
    <li><svg width="8" height="8" viewBox="0 0 8 8"><rect x=".5" y=".5" width="7" height="7" fill="none" stroke="#fd9900" stroke-width=".8"/><path d="M1.8 4l1.6 1.6L6.5 2" fill="none" stroke="#fd9900" stroke-width="1"/></svg>Promote diversity, equity, and inclusion throughout the industry</li>
  </ul>
  <div class="abs brand" style="left:254px;top:48px;font-size:13px">Pinecrest Artisan League</div>
  <div class="abs" style="left:254px;top:104px;width:155px">
    <div class="h2" style="line-height:17px">Diversity,<br>Equity &amp; Inclusion</div>
    <div class="rule" style="margin:5px 0 10px"></div>
    <div class="txt">The League promotes and encourages open dialogue and positive working environments for BIPOC and other identity groups, to thrive within a contractor community and facilitate a more inclusive and resilient future.</div>
    <div class="h2" style="margin-top:30px">About Us</div>
    <div class="rule" style="margin:5px 0 9px"></div>
    <div class="txt"><p>The League is organized as a 501c6 membership organization supported by a 501c3 charitable foundation. Our foundation allows us to provide access to training and education resources to an underserved community of contractors, supporting them in developing a sustainable and profitable business.</p><p>We invite you to join a community of contractors who are better prepared to overcome challenges within the industry, empowering them to share ideas, lessons learned, proven practices, and insights with other industry leaders.</p></div>
  </div>
  <div class="photo" style="left:0;top:443px;width:458px;height:150px;background:radial-gradient(ellipse 70% 90% at 70% 40%,#d9cfc2 0%,#a79a88 35%,#6f7c62 65%,#3f443b 100%)" role="img" aria-label="Modern home patio with outdoor chairs and an open kitchen"></div>
  <div class="footer light"><span class="site">pinecrestleague.org</span><span class="line"></span><span class="contact">hello@pinecrestleague.org &nbsp; 555-010-4821</span></div>
</div>

<!-- Page 2 -->
<div class="page" style="top:754px;background:#f7f7f7">
  <div class="photo" style="left:0;top:0;width:458px;height:593px;background:radial-gradient(ellipse 55% 50% at 80% 30%,#c9cbcd 0%,#e4e5e6 55%,rgba(247,247,247,0) 100%),radial-gradient(ellipse 45% 35% at 85% 85%,#a79d91 0%,#cfc9c1 50%,rgba(247,247,247,0) 100%),radial-gradient(ellipse 30% 25% at 10% 85%,#e0e0e0 0%,rgba(247,247,247,0) 100%)" role="img" aria-label="Desk flat lay with keyboard, phone, spiral notebook, pen and earphones"></div>
  <div class="abs" style="left:20px;top:0;width:207px;height:593px;background:rgba(255,255,255,.8)"></div>
  <div class="abs" style="left:47px;top:43px;width:158px">
    <div class="h2">Technical Assistance</div>
    <div class="rule" style="margin:5px 0 9px"></div>
    <div class="txt"><p>One of our primary goals is to provide technical assistance to the contractor community based on individual level of competency. We understand that the needs of contractors vary greatly based on experience, training, past mentorship.</p><p>Technical assistance takes many forms including business formation assistance, contractor licensing (OR, WA), insurance consulting, access to legal resources as well as assistance with government program funding (PPP Loans, business grants, scholarships), and various networking opportunities.</p><p>We also provide technical assistance in one-on-one setting as well as business workshops and ongoing assistance. Additionally, we offer assistance with CertifyBiz initial and renewal applications.</p></div>
    <div class="brand" style="margin-top:16px;font-size:10px">Pinecrest Artisan League</div>
  </div>
  <div class="footer"><span class="site">pinecrestleague.org</span><span class="line"></span><span class="contact">hello@pinecrestleague.org &nbsp; 555-010-4821</span></div>
</div>

<!-- Page 3 -->
<div class="page" style="top:1427px">
  <div class="abs" style="left:47px;top:40px;font-size:17px;font-weight:300;color:var(--orange)">Safety &amp; Compliance</div>
  <svg class="abs" style="left:0;top:96px" width="95" height="140" viewBox="0 0 95 140"><path d="M0 1H82l9 9M0 139H82l9-9" fill="none" stroke="#fd9900" stroke-width="1"/></svg>
  <div class="abs" style="left:95px;top:92px;display:flex;align-items:center;gap:4px;font-size:11px;font-weight:300;color:#444"><span style="width:9px;height:9px;border-radius:50%;background:var(--orange)"></span>SafeLedger</div>
  <div class="photo" style="left:47px;top:118px;width:146px;height:100px;background:radial-gradient(ellipse at 50% 45%,#cfe3f1 0%,#9fc0d8 50%,rgba(255,255,255,0) 80%)" role="img" aria-label="Safety log software shown on laptop, tablet and phone screens"></div>
  <div class="abs" style="left:229px;top:87px;width:182px">
    <div class="h2">SafeLedger</div>
    <div class="rule" style="margin:5px 0 9px"></div>
    <div class="txt" style="font-size:6.4px;line-height:9.8px"><p>SafeLedger.io is a secure, web-based application that enables employers to create each state's first report of injury, track injuries, and view injury metrics in real-time. The software includes the ability automatically generate and download PDF versions of OSHA forms 301, 300, and 300A to print, share, or email.</p><p>Works with all devices: computers, tablets, and smartphones. Once data is entered and intuitively updated on all other forms, SafeLedger will automatically generate benchmark figures with no additional input by location and log.</p></div>
  </div>
  <div class="abs" style="left:47px;top:269px;width:364px;height:1px;background:var(--rule)"></div>
  <div class="photo" style="left:210px;top:290px;width:248px;height:303px;background:radial-gradient(ellipse 55% 60% at 48% 55%,#e86a1c 0%,#e7874a 30%,#c9b07a 55%,rgba(255,255,255,0) 85%)" role="img" aria-label="Construction worker in orange hard hat and hi-vis jacket using a tablet, coworker beside him"></div>
  <div class="abs" style="left:47px;top:294px;width:182px">
    <div class="h2">CrewGuard</div>
    <div class="rule" style="margin:5px 0 9px"></div>
    <div class="txt" style="font-size:6.4px;line-height:9.8px">Our partnership with CrewGuard gives you the tools you need to protect your workers, meet compliance requirements, and create a positive workspace environment for your employees and others you may work with. CrewGuard's staff of safety professionals, safety trainers, and administrative staff combined with innovative technology has helped thousands of contractors across the nation save money and improve efficiency.</div>
    <div class="sub" style="margin-top:10px;font-size:6.2px;line-height:8px">INCLUDED IN THE MOBILE APP<br>ARE THE FOLLOWING:</div>
  </div>
  <ul class="abs ticks" style="left:51px;top:457px;width:165px;font-weight:500;font-size:6.2px;line-height:8.5px">
    <li style="margin-bottom:5px"><svg width="8" height="8" viewBox="0 0 8 8"><rect x=".5" y=".5" width="7" height="7" fill="none" stroke="#fd9900" stroke-width=".8"/><path d="M1.8 4l1.6 1.6L6.5 2" fill="none" stroke="#fd9900" stroke-width="1"/></svg>Over 1,200 bilingual (Spanish/English) safety lessons with digital signoff rosters</li>
    <li style="margin-bottom:5px"><svg width="8" height="8" viewBox="0 0 8 8"><rect x=".5" y=".5" width="7" height="7" fill="none" stroke="#fd9900" stroke-width=".8"/><path d="M1.8 4l1.6 1.6L6.5 2" fill="none" stroke="#fd9900" stroke-width="1"/></svg>An online form builder to create job and equipment-specific inspection forms</li>
    <li style="margin-bottom:5px"><svg width="8" height="8" viewBox="0 0 8 8"><rect x=".5" y=".5" width="7" height="7" fill="none" stroke="#fd9900" stroke-width=".8"/><path d="M1.8 4l1.6 1.6L6.5 2" fill="none" stroke="#fd9900" stroke-width="1"/></svg>Mobile-accessible document storage repository</li>
    <li style="margin-bottom:5px"><svg width="8" height="8" viewBox="0 0 8 8"><rect x=".5" y=".5" width="7" height="7" fill="none" stroke="#fd9900" stroke-width=".8"/><path d="M1.8 4l1.6 1.6L6.5 2" fill="none" stroke="#fd9900" stroke-width="1"/></svg>Live monthly webinars addressing safety topics</li>
  </ul>
  <div class="footer"><span class="site">pinecrestleague.org</span><span class="line"></span><span class="contact" style="color:#fff">hello@pinecrestleague.org &nbsp; 555-010-4821</span></div>
</div>

<!-- Page 4 -->
<div class="page" style="top:2102px">
  <div class="abs h2" style="left:47px;top:43px">Contractor Education</div>
  <div class="abs brand" style="left:254px;top:43px;font-size:10px">Pinecrest Artisan League</div>
  <div class="abs rule" style="left:47px;top:60px;width:364px"></div>
  <div class="abs" style="left:47px;top:72px;width:364px;font-size:7px;line-height:10px;font-weight:700;font-style:italic;color:#444">We provide education through live classes, training workshops, and via eLearning courses. We provide in-class training for EPA/RRP Certification, CPR/First Aid certification, Fall Protection certification, and the Oregon CCB 16-hour Pre-licensing training.</div>
  <div class="abs" style="left:47px;top:120px;width:155px">
    <div class="sub">ONLINE COURSES</div>
    <div class="txt" style="margin-top:5px">We also offer a full suite of online construction education courses to help contractors learn at their own pace and convenience. Courses are mobile-friendly and available in English or Spanish.</div>
    <div class="txt" style="margin-top:4px;font-style:italic">Our online course catalog includes:</div>
  </div>
  <svg class="abs" style="left:112px;top:236px" width="26" height="300" viewBox="0 0 26 300">
    <line x1="13" y1="0" x2="13" y2="290" stroke="#fd9900" stroke-width="1.2"/>
    <g fill="#fff" stroke="#fd9900" stroke-width="1.4">
      <circle cx="13" cy="12" r="11"/><circle cx="13" cy="57" r="11"/><circle cx="13" cy="102" r="11"/><circle cx="13" cy="147" r="11"/><circle cx="13" cy="192" r="11"/><circle cx="13" cy="237" r="11"/><circle cx="13" cy="282" r="11"/>
    </g>
    <g fill="none" stroke="#555" stroke-width=".9">
      <circle cx="13" cy="12" r="5"/><path d="M9 57h8M14 54l3 3-3 3M17 60H9"/><rect x="9" y="98" width="8" height="8"/><rect x="8" y="143" width="10" height="8"/><path d="M13 187l5 9H8z"/><circle cx="13" cy="234" r="2.5"/><path d="M13 287v-9M13 281c-3-3-5-2-5 0M13 281c3-3 5-2 5 0"/>
    </g>
  </svg>
  <div class="tl-label" style="left:154px;top:245px">OSHA 10 &amp; 30<br>training</div>
  <div class="tl-label" style="left:55px;top:289px;text-align:right;width:50px">Trade-specific<br>skills</div>
  <div class="tl-label" style="left:154px;top:334px">Safety<br>courses</div>
  <div class="tl-label" style="left:45px;top:379px;text-align:right;width:60px">Administrative<br>courses</div>
  <div class="tl-label" style="left:154px;top:427px">HAZWOPER</div>
  <div class="tl-label" style="left:45px;top:469px;text-align:right;width:60px">Construction<br>management</div>
  <div class="tl-label" style="left:154px;top:514px">Environmental<br>exposure</div>
  <div class="tl-label" style="left:97px;top:546px">And much more...</div>
  <div class="abs" style="left:254px;top:120px;width:160px">
    <div class="sub">BUSINESS SUCCESS COACHING</div>
    <div class="txt" style="margin-top:5px">We also offer targeted training tracks in specific skillsets to promote business development necessary to operate an efficient business.</div>
    <div class="txt" style="margin-top:4px;font-style:italic">Skillsets include:</div>
  </div>
  <div class="skill" style="top:222px"><svg width="18" height="14" viewBox="0 0 18 14"><rect x="1" y="3" width="16" height="10" fill="none" stroke="#fd9900"/></svg>Business operations</div>
  <div class="skill" style="top:248px"><svg width="18" height="14" viewBox="0 0 18 14"><path d="M9 1v12M3 4h12M3 4l-2 5h4zM15 4l-2 5h4z" fill="none" stroke="#fd9900"/></svg>Business Law &amp; Contracts</div>
  <div class="skill" style="top:274px"><svg width="18" height="14" viewBox="0 0 18 14"><circle cx="9" cy="7" r="6" fill="none" stroke="#fd9900"/></svg>Understanding Financials</div>
  <div class="skill" style="top:300px"><svg width="18" height="14" viewBox="0 0 18 14"><path d="M9 1l6 3v4c0 3-3 5-6 6-3-1-6-3-6-6V4z" fill="none" stroke="#fd9900"/></svg>Safety &amp; Compliance training</div>
  <div class="skill" style="top:326px"><svg width="18" height="14" viewBox="0 0 18 14"><circle cx="9" cy="7" r="2" fill="none" stroke="#fd9900"/><path d="M9 1v3M9 10v3M3 7h3M12 7h3" stroke="#fd9900"/></svg>Marketing &amp; Networking</div>
  <div class="skill" style="top:352px;border-bottom:none"><svg width="18" height="14" viewBox="0 0 18 14"><path d="M1 13V6h5v7M7 13V2h5v11M13 13V8h4v5" fill="none" stroke="#fd9900"/></svg>Business Management / HR</div>
  <div class="abs sub" style="left:254px;top:387px">LIVE CLASSES</div>
  <div class="photo" style="left:210px;top:400px;width:248px;height:193px;background:radial-gradient(ellipse 60% 65% at 55% 50%,#b3a58f 0%,#c9bfae 35%,#dedbd5 60%,rgba(255,255,255,0) 90%)" role="img" aria-label="Adult student writing notes in a live classroom session"></div>
  <div class="footer"><span class="site">pinecrestleague.org</span><span class="line"></span><span class="contact">hello@pinecrestleague.org &nbsp; 555-010-4821</span></div>
</div>

<!-- Page 5 -->
<div class="page" style="top:2776px">
  <div class="abs h2" style="left:47px;top:43px">BuildFinder List</div>
  <div class="abs brand" style="left:254px;top:43px;font-size:10px">Pinecrest Artisan League</div>
  <div class="abs rule" style="left:47px;top:60px;width:364px"></div>
  <div class="abs txt" style="left:47px;top:78px;width:364px"><p><b style="color:#333">BuildFinderList.com</b> is a FREE effortless way for contractors to connect with property owners to search for a contractor in their local area. As marketing has evolved, contractors need to adopt a variety of online tools and technologies to help gain more online visibility which will result in more business for you.</p><p>The site gives instant access to residential and commercial contractors, an online bid request system, links to the contractor's social media pages and a review system all in one spot.</p><p>Create your business profile and easily manage your unlimited FREE Bid requests, reviews, social media, photo gallery, video clips just to name a few. Having a profile listing adds legitimacy to your business.</p><p>A prime advantage of having your business listed is the SEO and relevant incoming "links to your business". Link building is an important building block of any SEO campaign.</p></div>
  <svg class="abs" style="left:0;top:380px" width="458" height="213" viewBox="0 0 458 213"><path d="M0 110L458 8V28L0 130z" fill="#fd9900"/><path d="M0 130L458 28V213H0z" fill="#f3f1ec"/></svg>
  <div class="photo" style="left:110px;top:238px;width:348px;height:355px;background:radial-gradient(ellipse 45% 40% at 60% 20%,#f5c400 0%,#f0d35a 35%,rgba(255,255,255,0) 75%),radial-gradient(ellipse 60% 55% at 55% 65%,#b88a5a 0%,#c9a77d 40%,rgba(243,241,236,0) 80%)" role="img" aria-label="Contractor in yellow hard hat and tool belt working on a laptop at a workbench with tools"></div>
  <div class="abs" style="left:47px;top:276px;display:flex;align-items:center;gap:5px">
    <span style="width:12px;height:12px;border-radius:50%;background:var(--orange)"></span>
    <span style="font-size:9px;font-weight:600;color:var(--orange);line-height:10px">BUILDFINDER<br>LIST</span>
  </div>
  <div class="abs" style="left:52px;top:294px;width:0;height:120px;border-left:1px dashed #999"></div>
  <div class="footer"><span class="site">pinecrestleague.org</span><span class="line"></span><span class="contact">hello@pinecrestleague.org &nbsp; 555-010-4821</span></div>
</div>

<!-- Back cover -->
<div class="thumb" style="left:913px;top:3191px">
  <div class="abs" style="left:9px;top:9px;font-size:3.4px;line-height:5px;color:#555;width:60px">Build skills. Build safety. Build community. Join today at pinecrestleague.org</div>
  <div class="abs" style="left:9px;top:34px;font-size:3.2px;line-height:5px;color:#777;border-left:1px solid var(--orange);padding-left:3px">hello@pinecrestleague.org<br>555-010-4821</div>
  <div class="photo" style="left:0;top:52px;width:138px;height:107px;background:radial-gradient(ellipse at 30% 60%,#f6c25a 0%,#d98a2a 30%,#6a5a52 65%,#2f4d6a 100%)" role="img" aria-label="Building frame under construction at sunset"></div>
  <div class="abs brand" style="left:13px;top:166px;font-size:4.6px">Pinecrest Artisan League</div>
  <div class="abs" style="left:92px;top:167px;font-size:3.2px;color:#777">pinecrestleague.org</div>
</div>

</body>
</html>
```